Ferrant Valley Zoning Council Business Cards

We're looking for a business card design, simple as that. We're a local government agency that mainly performs building code enforcement, transportation planning, floodplain management, and GIS for Tobelle Parish in Louisiana, and other surround parishes. So you're not having to Google anything, GIS is, at it's core, mapping. Building Code Enforcement is just that, nothing more. Floodplain Management is to make sure the public is within what the government

Contact Information for Business Card

Our Address is

517 Marwick Street
Tobelle City, TB 71489

Our phone is 3185529137
Our fax is 3185529142
Our website is www.fvzc.info
My email is dana@fvzc.info

Font styles to use
Serif
Sans Serif

Colors

Designer to choose colors to be used in the design.

Requirements
Must have
• I'm attaching our logo(several versions) that must be incorporated. The design should fit well with our existing logo. I can send photoshop files for our logo if needed. If possible, I'd like to be able to add names/info to each card for all of our employees once this is done.
Nice to have
• The Louisiana state seal is a bonus, and isn't specifically required.

```html
<!DOCTYPE html>
<html lang="en">
<head>
<meta charset="UTF-8">
<title>Ferrant Valley Zoning Council – Business Cards</title>
<link href="https://fonts.googleapis.com/css2?family=Montserrat:wght@400;500;700&display=swap" rel="stylesheet">
<style>
  :root {
    --backdrop: #2b2b2d;
    --card: #1f1f21;
    --white: #ffffff;
    --muted: #cfcfcf;
    --rule: #9a9a9a;
    --accent-lime: #d6f01c;
    --blue: #1f4fd6;
    --green: #38b63a;
    --orange: #f39212;
    --lime: #c9e41a;
    --seal-blue: #1d4f8f;
  }
  * { box-sizing: border-box; margin: 0; padding: 0; }
  html, body { width: 1200px; height: 1108px; overflow: hidden; }
  body {
    background: var(--backdrop);
    font-family: "Montserrat", sans-serif;
    color: var(--white);
    position: relative;
  }
  .card {
    position: absolute;
    top: 150px;
    width: 460px;
    height: 805px;
    border-radius: 26px;
    background: var(--card);
    box-shadow: 0 18px 40px rgba(0,0,0,.45);
    overflow: hidden;
  }
  .card--front { left: 110px; }
  .card--back { left: 630px; }

  /* Front */
  .brand {
    position: absolute; top: 120px; left: 0; right: 0;
    display: flex; flex-direction: column; align-items: center;
  }
  .brand__row { display: flex; align-items: center; gap: 16px; }
  .brand__mark { width: 58px; height: 58px; background: var(--blue); border-radius: 6px; }
  .brand__name { font-size: 76px; font-weight: 700; letter-spacing: 2px; line-height: 1; }
  .brand__caption { font-size: 12px; color: var(--muted); margin-top: 8px; letter-spacing: .5px; }

  .person { position: absolute; top: 372px; left: 0; right: 0; text-align: center; }
  .person__name { font-size: 30px; font-weight: 700; color: var(--accent-lime); letter-spacing: 1px; }
  .person__title { font-size: 19px; font-weight: 500; margin-top: 2px; }

  .divider { position: absolute; left: 95px; right: 95px; height: 1px; background: var(--rule); }
  .divider--top { top: 474px; }
  .divider--mid { top: 640px; left: 70px; right: 70px; }

  .contact-icons {
    position: absolute; top: 458px; left: 0; right: 0;
    display: flex; justify-content: center; gap: 6px;
  }
  .contact-icons svg { width: 30px; height: 30px; }

  .contacts {
    position: absolute; top: 505px; left: 0; right: 0;
    text-align: center; font-size: 20px; line-height: 30px; font-weight: 500;
  }
  .address {
    position: absolute; top: 660px; left: 0; right: 0;
    text-align: center; font-size: 20px; line-height: 30px; font-weight: 500;
  }

  /* Back */
  .pattern-field {
    position: absolute; top: 0; left: 0; right: 0; height: 600px;
    background:
      linear-gradient(180deg, rgba(31,31,33,0) 55%, var(--card) 100%),
      linear-gradient(135deg, #3a3f20 0%, #24315a 30%, #2f4a26 55%, #4a3a1c 80%, #2a2f45 100%);
    opacity: .8;
  }
  .back-brand {
    position: absolute; top: 470px; right: 58px;
    display: flex; align-items: center; gap: 12px;
  }
  .back-brand__mark { width: 34px; height: 34px; background: var(--green); border-radius: 4px; }
  .back-brand__name { font-size: 40px; font-weight: 700; letter-spacing: 1px; }
  .seal {
    position: absolute; top: 600px; left: 50%; transform: translateX(-50%);
    width: 170px; height: 170px;
  }
</style>
</head>
<body>

  <section class="card card--front">
    <div class="brand">
      <div class="brand__row">
        <span class="brand__mark"></span>
        <span class="brand__name">FVZC</span>
      </div>
      <p class="brand__caption">Ferrant Valley Zoning Council</p>
    </div>

    <div class="person">
      <h1 class="person__name">EVAN HARLOW</h1>
      <p class="person__title">Manager</p>
    </div>

    <div class="divider divider--top"></div>
    <div class="contact-icons">
      <svg viewBox="0 0 30 30" aria-label="Phone"><circle cx="15" cy="15" r="14" fill="var(--blue)"/><path d="M10 9c1-1 2 0 3 2s-1 2 0 3l2 2c1 1 1-1 3 0s3 2 2 3c-2 3-6 1-9-2s-4-6-1-8z" fill="#fff"/></svg>
      <svg viewBox="0 0 30 30" aria-label="Fax"><circle cx="15" cy="15" r="14" fill="var(--green)"/><rect x="9" y="13" width="12" height="7" rx="1" fill="#fff"/><rect x="11" y="9" width="8" height="5" fill="#fff"/><rect x="11" y="18" width="8" height="4" fill="var(--green)" stroke="#fff"/></svg>
      <svg viewBox="0 0 30 30" aria-label="Email"><circle cx="15" cy="15" r="14" fill="var(--orange)"/><rect x="8" y="10" width="14" height="10" rx="1" fill="#fff"/><path d="M8 10l7 6 7-6" fill="none" stroke="var(--orange)" stroke-width="1.5"/></svg>
      <svg viewBox="0 0 30 30" aria-label="Website"><circle cx="15" cy="15" r="14" fill="var(--lime)"/><circle cx="15" cy="15" r="7" fill="none" stroke="#222" stroke-width="1.5"/><path d="M8 15h14M15 8c-3 4-3 10 0 14M15 8c3 4 3 10 0 14" fill="none" stroke="#222" stroke-width="1.2"/></svg>
    </div>

    <div class="contacts">
      <p>3185529137</p>
      <p>3185529142</p>
      <p>dana@fvzc.info</p>
      <p>www.fvzc.info</p>
    </div>

    <div class="divider divider--mid"></div>
    <div class="address">
      <p>517 Marwick Street</p>
      <p>Tobelle City, TB 71489</p>
    </div>
  </section>

  <section class="card card--back">
    <div class="pattern-field" role="img" aria-label="Faint honeycomb pattern of coloured hexagon tiles"></div>
    <div class="back-brand">
      <span class="back-brand__mark"></span>
      <span class="back-brand__name">FVZC</span>
    </div>
    <svg class="seal" viewBox="0 0 170 170" aria-hidden="true">
      <circle cx="85" cy="85" r="84" fill="#fff"/>
      <circle cx="85" cy="85" r="76" fill="var(--seal-blue)"/>
      <circle cx="85" cy="85" r="50" fill="none" stroke="#fff" stroke-width="2"/>
    </svg>
  </section>

</body>
</html>
```